Redesign Home Page

We need a new home page with a white background. Our company provides singing instruction to students world wide, both in person and on line. We're looking for a very clean and open design with maximum white space. The main goal of the page will be to get users to sign up for our mailing list. The current site is www.kelvarsong.com. I think the new page can be a long page (scrolll down is ok), to allow for more white space while still using the text from the current page.
Updates

Project Deadline Extended
Reason: Hello to all Designers, I apologize for not giving feedback this weekend. We went out of town for the Memorial Day holiday and I had no internet. I will be extending the deadline to Thursday. -Marcus

Target Market(s)

Singers of all ages and abilities, especially beginners.

Industry/Entity Type

It Company

Requirements
Must have
• 1. A white background
2. Lots of open space
3. An email sign up form on the top right that reads:
a. “Improve Your Singing Now.
b. Sign up for our Free Video Series: Tone Pathway
4. Testimonails: found on https://www.kelvarsong.com/tone-ascent
5. My logo with the piano
6. My photo
7. Learn about our Lessons in:
a. San Francisco
b. Alameda
8. On Line Programs:
a. Tone Ascent
b. Zelvo Lessons

Nice to have
• Link to current student page: http://kelvarsong.com/what-students-say/students2
Pictures of singers
Video box: Use Marcus_Example
Should not have
• See "KelvarSong Redesign" file for more details.

```html
<!DOCTYPE html>
<html lang="en">
<head>
<meta charset="utf-8">
<title>MarcusHale School of Voice</title>
<link href="https://fonts.googleapis.com/css2?family=Open+Sans:ital,wght@0,400;0,600;0,700;1,400&display=swap" rel="stylesheet">
<style>
:root{
  --blue:#29a9e1;
  --blue-dark:#1b97d0;
  --blue-light:#5fcdf3;
  --ink:#333;
  --grey:#666;
  --muted:#8a8a8a;
  --bar:#2b2b2b;
  --footer:#ececec;
  --line:#d4d4d4;
}
*{box-sizing:border-box;margin:0;padding:0}
html,body{width:954px;height:1200px;overflow:hidden;background:#fff}
body{position:relative;font-family:"Open Sans",Arial,sans-serif;color:var(--ink)}
.abs{position:absolute}
.top-bar{left:0;top:0;width:954px;height:10px;background:var(--bar)}
.brand{left:146px;top:30px;display:flex;align-items:center;gap:10px}
.brand-mark{width:20px;height:20px;background:var(--blue)}
.brand-name{font-size:28px;font-weight:400;color:var(--ink);line-height:1}
.brand-sub{left:251px;top:72px;font-size:14px;color:var(--ink)}
.call{left:567px;top:55px;font-size:13px;color:var(--ink);letter-spacing:.3px}
.call span{color:var(--blue)}
.login{left:710px;top:48px;width:110px;height:30px;background:linear-gradient(#4a4a4a,#333);border-radius:2px;color:#fff;font-size:13px;display:flex;align-items:center}
.login .ico{width:30px;height:30px;display:flex;align-items:center;justify-content:center;background:#2a2a2a}
.login .lbl{flex:1;text-align:center}
.nav{left:0;top:105px;width:954px;height:36px;background:linear-gradient(#36b3e8,var(--blue-dark))}
.nav ul{list-style:none;position:absolute;left:138px;top:0;display:flex;height:36px}
.nav li{color:#fff;font-size:11.5px;font-weight:600;padding:0 12px;line-height:36px}
.nav li.active{background:var(--blue-light)}
.hero{left:0;top:141px;width:954px;height:423px;background:linear-gradient(90deg,#dcdcdc,#ececec 50%,#e4e4e4)}
.hero-photo{left:122px;top:141px;width:396px;height:423px;background:linear-gradient(#d9c3b3 0,#c9ab97 38%,#1c1c1c 45%,#151515)}
.signup{left:463px;top:210px;width:357px;height:142px;background:linear-gradient(#fff,#e9e9e9);border:1px solid #d0d0d0;border-radius:2px;text-align:center}
.signup .kicker{margin-top:17px;font-size:10.5px;color:var(--ink)}
.signup h2{margin-top:6px;font-size:21px;font-weight:700;color:var(--blue)}
.signup .field{position:absolute;top:86px;width:118px;height:24px;background:#fff;border:1px solid #d2d2d2;font-size:8.5px;color:#555;text-align:left;padding:6px 7px}
.signup .go{position:absolute;left:264px;top:86px;width:79px;height:24px;background:var(--blue);color:#fff;font-size:8.5px;font-weight:700;line-height:24px}
.slider{left:593px;top:383px;width:123px;height:20px;background:#f4f4f4;border:1px solid #aab6c6;border-radius:3px;display:flex;align-items:center}
.slider .arrows{width:36px;display:flex;justify-content:center;gap:6px;border-right:1px solid #ccc;height:100%;align-items:center}
.slider .dots{display:flex;gap:6px;padding-left:10px}
.dot{width:6px;height:6px;border-radius:50%;background:#999}
.dot.on{background:#222}
.section-title{font-size:13.5px;color:var(--ink);letter-spacing:.2px}
.pic{background:linear-gradient(#a8c6e6,#8aa7c4 60%,#5d7d48)}
.pic.night{background:linear-gradient(#1f2a3a,#3a2a1e 55%,#a05a22)}
.pic.video{background:radial-gradient(circle at 55% 50%,#4c4c4c,#222 70%)}
.loc-name{font-size:14px;color:var(--blue)}
.btn{width:68px;height:17px;border-radius:3px;font-size:7.5px;font-weight:700;color:#fff;display:flex;align-items:center;justify-content:center;gap:4px}
.btn.email{background:linear-gradient(#7fb6ea,#4d8fd3)}
.btn.hours{background:#333}
.addr{font-size:7.5px;color:var(--muted)}
.phone{font-size:17px;color:#888}
.arrow-box{width:14px;height:13px;background:#666;display:flex;align-items:center;justify-content:center}
.t-photo{width:75px;height:53px;border:1px solid #ccc;background:linear-gradient(#e6d2c4,#b98f78)}
.t-photo.dark{background:linear-gradient(#4a3c30,#2a221c);border-color:#444}
.t-name{font-size:14px;color:var(--blue)}
.t-city{font-size:11px;font-style:italic;color:var(--ink)}
.t-quote{width:188px;font-size:8px;line-height:15px;color:var(--muted);text-align:justify}
.q{font-size:13px;color:#666;font-weight:700;line-height:1}
.footer{left:0;top:1059px;width:954px;height:141px;background:var(--footer)}
.links{left:0;top:1082px;width:954px;text-align:center;font-size:8.5px;color:var(--ink)}
.copy{left:142px;top:1134px;font-size:8px;color:#444}
.social{left:385px;top:1122px;display:flex;gap:6px}
.social span{width:27px;height:27px;border-radius:50%;background:#5a5a5a;display:block}
.news{left:653px;top:1127px;width:165px;height:21px;background:#fff;border:1px solid #bbb;font-size:8px;color:#555;padding:5px 6px}
.news svg{position:absolute;right:3px;top:3px}
</style>
</head>
<body>
<div class="abs top-bar"></div>

<header>
  <div class="abs brand"><span class="brand-mark"></span><span class="brand-name" style="margin-left:70px">MarcusHale</span></div>
  <div class="abs brand-sub">School of Voice</div>
  <div class="abs call"><span>CALL :</span> 250-555-0143</div>
  <div class="abs login">
    <span class="ico"><svg width="13" height="13" viewBox="0 0 13 13"><circle cx="6.5" cy="3.5" r="3" fill="#fff"/><path d="M1 13c0-4 2.5-5.5 5.5-5.5S12 9 12 13z" fill="#fff"/></svg></span>
    <span class="lbl">LOG IN</span>
  </div>
</header>

<nav class="abs nav">
  <ul>
    <li class="active">HOME</li><li>VOICE LESSONS</li><li>BLOG</li><li>WHAT STUDENTS SAY</li><li>MEET THE INSTRUCTORS</li><li>TONE ASCENT</li>
  </ul>
</nav>

<section>
  <div class="abs hero" role="img" aria-label="Light grey studio backdrop"></div>
  <div class="abs hero-photo" role="img" aria-label="Photo of the voice teacher in a black turtleneck"></div>
  <div class="abs signup">
    <p class="kicker">Sign up for our free video Series:</p>
    <h2>Tone Pathway</h2>
    <div class="field" style="left:16px">First Name</div>
    <div class="field" style="left:140px">Email</div>
    <div class="go">GET STARTED</div>
  </div>
  <div class="abs slider">
    <div class="arrows">
      <svg width="6" height="8" viewBox="0 0 6 8"><path d="M5 0.5 1.5 4 5 7.5" stroke="#222" stroke-width="1.6" fill="none"/></svg>
      <svg width="6" height="8" viewBox="0 0 6 8"><path d="M1 0.5 4.5 4 1 7.5" stroke="#888" stroke-width="1.6" fill="none"/></svg>
    </div>
    <div class="dots"><span class="dot"></span><span class="dot"></span><span class="dot on"></span><span class="dot"></span><span class="dot"></span><span class="dot"></span></div>
  </div>
</section>

<section>
  <h3 class="abs section-title" style="left:140px;top:595px">ABOUT OUR LESSONS</h3>
  <h3 class="abs section-title" style="left:599px;top:595px">ON LINE</h3>

  <div class="abs pic" style="left:138px;top:625px;width:218px;height:123px" role="img" aria-label="Alameda shoreline with city skyline"></div>
  <div class="abs pic night" style="left:369px;top:625px;width:218px;height:123px" role="img" aria-label="Bridge in San Francisco at night"></div>
  <div class="abs pic video" style="left:598px;top:625px;width:222px;height:123px" role="img" aria-label="Online video lesson preview"></div>
  <svg class="abs" style="left:695px;top:667px" width="40" height="40" viewBox="0 0 40 40"><circle cx="20" cy="20" r="18" fill="none" stroke="#fff" stroke-width="3"/><path d="M15 11 29 20 15 29z" fill="#fff"/></svg>

  <div class="abs loc-name" style="left:139px;top:752px">Alameda</div>
  <div class="abs btn email" style="left:286px;top:753px"><svg width="9" height="7" viewBox="0 0 9 7"><rect width="9" height="7" fill="#fff"/><path d="M0 0 4.5 4 9 0" stroke="#4d8fd3" fill="none"/></svg>Email Us</div>
  <div class="abs btn hours" style="left:286px;top:775px">Working Hours</div>
  <div class="abs addr" style="left:139px;top:781px">Near Linden Way and Grove</div>
  <div class="abs phone" style="left:139px;top:788px">510-555-0182</div>

  <div class="abs loc-name" style="left:370px;top:752px">San Francisco</div>
  <div class="abs btn email" style="left:519px;top:753px"><svg width="9" height="7" viewBox="0 0 9 7"><rect width="9" height="7" fill="#fff"/><path d="M0 0 4.5 4 9 0" stroke="#4d8fd3" fill="none"/></svg>Email Us</div>
  <div class="abs btn hours" style="left:519px;top:775px">Working Hours</div>
  <div class="abs addr" style="left:370px;top:781px">418 Harbor ST # 210</div>
  <div class="abs phone" style="left:369px;top:788px">510-555-0182</div>
</section>

<section>
  <h3 class="abs section-title" style="left:141px;top:850px">TESTIMONIALS</h3>
  <div class="abs arrow-box" style="left:792px;top:850px"><svg width="6" height="8" viewBox="0 0 6 8"><path d="M5 .5 1.5 4 5 7.5" stroke="#fff" fill="none"/></svg></div>
  <div class="abs arrow-box" style="left:807px;top:850px"><svg width="6" height="8" viewBox="0 0 6 8"><path d="M1 .5 4.5 4 1 7.5" stroke="#fff" fill="none"/></svg></div>

  <div class="abs t-photo" style="left:149px;top:891px" role="img" aria-label="Student portrait"></div>
  <div class="abs t-name" style="left:233px;top:893px">DANA WHITLOW</div>
  <div class="abs t-city" style="left:233px;top:915px">San Francoco</div>
  <div class="abs q" style="left:148px;top:950px">&ldquo;</div>
  <p class="abs t-quote" style="left:159px;top:949px">Lorem Ipsum is simply dummy text of the printing and typesetting industry. Lorem Ipsum has been the industry's standard dummy text ever since the printing and typesetting industry. Lorem Ipsum has the 1500s Lorem Ipsum has been text ever <span class="q">&rdquo;</span></p>

  <div class="abs t-photo dark" style="left:381px;top:891px" role="img" aria-label="Student portrait"></div>
  <div class="abs t-name" style="left:465px;top:893px">DANA WHITLOW</div>
  <div class="abs t-city" style="left:465px;top:915px">San Francoco</div>
  <div class="abs q" style="left:378px;top:950px">&ldquo;</div>
  <p class="abs t-quote" style="left:389px;top:949px">Lorem Ipsum is simply dummy text of the printing and typesetting industry. Lorem Ipsum has been the industry's standard dummy text ever since the printing and typesetting industry. Lorem Ipsum has the 1500s Lorem Ipsum has been text ever <span class="q">&rdquo;</span></p>

  <div class="abs t-photo dark" style="left:613px;top:891px" role="img" aria-label="Student portrait"></div>
  <div class="abs t-name" style="left:697px;top:893px">DANA WHITLOW</div>
  <div class="abs t-city" style="left:697px;top:915px">San Francoco</div>
  <div class="abs q" style="left:611px;top:952px">&ldquo;</div>
  <p class="abs t-quote" style="left:622px;top:951px">Lorem Ipsum is simply dummy text of the printing and typesetting industry. Lorem Ipsum has been the industry's standard dummy text ever since the printing and typesetting industry. Lorem Ipsum has the 1500s Lorem Ipsum has been text ever <span class="q">&rdquo;</span></p>
</section>

<footer>
  <div class="abs footer"></div>
  <div class="abs links">Terms of Service | Returns | Policy Privacy | Event | Contact | Blog | Sitemap</div>
  <div class="abs copy">Copy Right © 2014. All rights reserved.</div>
  <div class="abs social" aria-label="Social links"><span></span><span></span><span></span><span></span><span></span><span></span></div>
  <div class="abs news">News Letter
    <svg width="22" height="14" viewBox="0 0 22 14"><rect width="22" height="14" fill="#222"/><path d="M1 1 11 8 21 1" stroke="#fff" stroke-width="1.5" fill="none"/></svg>
  </div>
</footer>
</body>
</html>
```